Broschüre für Gleichstellungsstelle einer kommunalen Stadtverwaltung
Zielgruppe
Wir sind die Gleichstellungsstelle einer kommunalen Stadtverwaltung (Einwohner*innen ca. 74.500) und richten uns mit unserer Arbeit grundsätzlich an alle Menschen.
Wir wollen eine Broschüre zum Handlungsleitfaden für die geschlechtergerechte Sprache bei der Stadt erstellen. Dieser soll an die Beschäftigten als Unterstützung verteilt werden.
Aufgabenstellung
- Broschüre mit Wire-O-Bindung, Druckformat 14,8 cm x 14,8 cm, Endformat 15,0 x 15,0 cm
- Spiralbindung an der Kopfseite
- doppelseitiges Deckblatt und Rückseite
- 16 Seiten Inhalt, wobei lediglich die Vorderseiten Text enthalten
- Schriftart (optimal Avenir Next, alternativ Arial) und Farbschema laut Corporate Design
- Der Text ist vorgegeben, die Gestaltung ist im Rahmen des Corporate Designs frei
Es soll eine ansprechende Broschüre gestaltet werden, welche die Leser*innen zum Blättern einlädt. Das bedeutet, dass alle Seiten (Deckblatt, Inhaltsseiten und Rückseiten) bei der Gestaltung berücksichtigt werden müssen.
Am Ende soll neben den üblichen Dateien auch eine fertige Druckdatei (siehe Datenblatt) zur Verfügung gestellt werden. Dabei ist zu beachten, dass die Spiralbindung des fertigen Produkts an der Kopfseite sein soll.

```html
<!DOCTYPE html>
<html lang="de">
<head>
<meta charset="utf-8">
<title>Gendersternchen</title>
<link href="https://fonts.googleapis.com/css2?family=Nunito+Sans:wght@400;600;700;800&display=swap" rel="stylesheet">
<style>
  :root {
    --green-dark: #005048;
    --green-soft: #98b3ae;
    --green-highlight: #aecbc5;
    --text-grey: #6a6a6a;
    --white: #ffffff;
  }
  html, body {
    margin: 0;
    padding: 0;
    overflow: hidden;
    background: var(--white);
  }
  .page {
    position: relative;
    width: 1200px;
    height: 1200px;
    background: var(--white);
    font-family: "Nunito Sans", "Avenir Next", Arial, sans-serif;
    overflow: hidden;
  }
  .intro {
    position: absolute;
    left: 0; top: 0;
    width: 1200px;
    height: 424px;
    background: var(--green-dark);
    color: var(--white);
  }
  .intro__title {
    position: absolute;
    left: 81px; top: 126px;
    margin: 0;
    font-size: 36px;
    font-weight: 800;
    letter-spacing: 0.5px;
  }
  .intro__text {
    position: absolute;
    left: 81px; top: 182px;
    margin: 0;
    font-size: 26px;
    line-height: 40px;
    font-weight: 400;
  }
  .intro__highlight {
    color: var(--green-highlight);
    font-weight: 700;
  }
  .example {
    position: absolute;
    height: 73px;
    background: var(--green-soft);
    color: var(--white);
    font-size: 34px;
    font-weight: 600;
    line-height: 73px;
    padding-left: 16px;
    box-sizing: border-box;
    white-space: nowrap;
  }
  .example--a { left: 64px;  top: 479px; width: 450px; }
  .example--b { left: 592px; top: 479px; width: 450px; }
  .example--c { left: 64px;  top: 566px; width: 450px; }
  .example--d { left: 592px; top: 566px; width: 450px; }
  .tip {
    position: absolute;
    left: 0; top: 682px;
    width: 919px;
    height: 216px;
    background: var(--green-dark);
    color: var(--white);
  }
  .tip__icon {
    position: absolute;
    left: 44px; top: 30px;
  }
  .tip__title {
    position: absolute;
    left: 120px; top: 26px;
    margin: 0;
    font-size: 28px;
    font-weight: 800;
  }
  .tip__text {
    position: absolute;
    left: 120px; top: 70px;
    margin: 0;
    font-size: 28px;
    line-height: 43px;
    font-weight: 400;
  }
  .pronunciation {
    position: absolute;
    left: 81px; top: 926px;
    margin: 0;
    color: var(--text-grey);
    font-size: 26px;
    line-height: 40px;
  }
  .pronunciation-example {
    position: absolute;
    left: 276px; top: 1063px;
    width: 631px;
    height: 74px;
    background: var(--green-soft);
    color: var(--white);
    font-size: 34px;
    font-weight: 600;
    line-height: 74px;
    text-align: center;
  }
</style>
</head>
<body>
<main class="page">
  <section class="intro">
    <h1 class="intro__title">GENDERSTERNCHEN</h1>
    <p class="intro__text">
      Das Gendersternchen dient als <span class="intro__highlight">sprachliches Darstellungsmittel</span> aller<br>
      Geschlechter und Geschlechtsidentitäten:<br>
      Im Schriftlichen wird das Sternchen (*) zwischen die maskuline und<br>
      feminine Endung eines Wortes eingesetzt, auch bei Artikeln und<br>
      Pronomen. Zum Beispiel:
    </p>
  </section>

  <div class="example example--a">der*die Mitarbeiter*in</div>
  <div class="example example--b">die Mitarbeiter*innen</div>
  <div class="example example--c">ein*e Mitarbeiter*in</div>
  <div class="example example--d">jede*r Mitarbeiter*in</div>

  <aside class="tip">
    <svg class="tip__icon" width="48" height="162" viewBox="0 0 48 162" aria-hidden="true">
      <rect x="4" y="2" width="40" height="104" fill="#ffffff"/>
      <circle cx="24" cy="138" r="22" fill="#ffffff"/>
    </svg>
    <h2 class="tip__title">TIPP:</h2>
    <p class="tip__text">
      Greifen Sie nach Möglichkeit bei der Formulierung<br>
      mit Gendersternchen auf die Pluralform zurück, dabei<br>
      muss der Artikel in der Regel nicht gegendert werden.
    </p>
  </aside>

  <p class="pronunciation">
    Das Gendersternchen (*) wird mit einer kurzen stimmlosen Pause ge-<br>
    sprochen, auch Verschlusslaut, glottaler Schlag oder kurz Glottisschlag<br>
    genannt. Zum Beispiel:
  </p>

  <div class="pronunciation-example">Mitarbeiter [kurze Pause] innen</div>
</main>
</body>
</html>
```